Marrow Business Cards

Front of business card will have logo, name, address, & telephone number. Back of card will have a list of services provided - Roads, Substation Pads, Temporary Pads, Site Pads, Land Leveling, Powerline Row Cleaning, Land Clearing, Gates, Fencing, Construction Entrances, Excavation, Trenching, Underground Utilities, Directional Boring, Pile Driving. We are a construction company that uses heavy equipment like bulldozers, motor graders/blades, dump trucks, backhoes, hydro axes, & skid loaders. We build roads, pads, & install electric utility lines & waterlines underground. This logo is new. The word "Construction" can be smaller as uploaded 2 example edited logos. We will be using this card design for many employees.
Target Market(s)
Industrial Electric Powerline, Wind Turbine, Solar Panel, & Water Utility companies.
Contact Information for Business Card
Name/Position - Dorian Quale - Owner
Address: 4837 FM 582
Larkmoor, OK 73419
Phone number - (555) 418-2906

```html
<!DOCTYPE html>
<html lang="en">
<head>
<meta charset="utf-8">
<title>Marrow Construction Business Cards</title>
<link href="https://fonts.googleapis.com/css2?family=Roboto:wght@300;400;500&display=swap" rel="stylesheet">
<style>
  :root{
    --backdrop:#e6e6e6;
    --card:#2f2f30;
    --card-edge:#5a1f2c;
    --ink:#f2f2f2;
    --ink-soft:#c9c9c9;
    --ink-muted:#8d8d8d;
    --rule:#7a7a7a;
    --mark-fill:#6b6b6b;
  }
  *{box-sizing:border-box;margin:0;padding:0}
  html,body{width:1200px;height:801px;overflow:hidden}
  body{
    background:var(--backdrop);
    font-family:"Roboto",sans-serif;
    display:flex;align-items:center;justify-content:center;gap:40px;
  }
  .card{
    position:relative;width:540px;height:309px;
    background:var(--card);color:var(--ink);
    border-bottom:2px solid var(--card-edge);
    box-shadow:0 8px 22px rgba(0,0,0,.25);
    overflow:hidden;
  }
  /* front */
  .card-front .brand{
    position:absolute;left:30px;top:0;bottom:0;width:230px;
    display:flex;align-items:center;justify-content:center;gap:10px;
  }
  .brand-dot{width:14px;height:14px;border-radius:50%;background:var(--ink);flex:none}
  .brand-name{font-weight:400;font-size:19px;letter-spacing:.08em;text-transform:uppercase;line-height:1.3;white-space:nowrap}
  .divider{position:absolute;left:272px;top:70px;width:1px;height:170px;background:var(--rule)}
  .contact{position:absolute;left:300px;top:70px;font-size:13px;line-height:1.45;color:var(--ink-soft)}
  .contact .person{font-size:17px;font-weight:500;color:var(--ink)}
  .contact .role{font-weight:300;margin-bottom:12px}
  .contact .address{font-weight:300;margin-bottom:12px}
  .contact .line{display:flex;align-items:center;gap:8px;font-weight:300;white-space:nowrap}
  .contact svg{width:11px;height:11px;fill:none;stroke:var(--ink-soft);stroke-width:1.6;flex:none}
  /* back */
  .services{
    position:absolute;right:34px;top:30px;text-align:right;
    font-size:15px;font-weight:300;line-height:1.3;color:var(--ink-soft);
    white-space:nowrap;
  }
  .services .lead{color:var(--ink-muted)}
  .services .gap{height:14px}
  .back-mark{
    position:absolute;left:0;bottom:0;width:230px;height:130px;
    background:linear-gradient(135deg,#3a3a3b,var(--mark-fill));
    clip-path:polygon(0 20%,60% 0,100% 15%,85% 100%,0 100%);
    opacity:.6;
  }
  .back-brand{
    position:absolute;right:34px;bottom:42px;display:flex;align-items:center;gap:10px;
  }
</style>
</head>
<body>
  <section class="card card-front">
    <div class="brand">
      <span class="brand-dot"></span>
      <span class="brand-name">Marrow<br>Construction</span>
    </div>
    <div class="divider"></div>
    <div class="contact">
      <p class="person">Dorian Quale</p>
      <p class="role">Owner</p>
      <p class="address">4837 FM 582<br>Larkmoor, OK 73419</p>
      <p class="line"><svg viewBox="0 0 12 12"><path d="M3 1l2 2-1 2 3 3 2-1 2 2-2 2C5 11 1 7 1 3z"/></svg>(555) 418-2906</p>
      <p class="line"><svg viewBox="0 0 12 12"><rect x="1" y="2.5" width="10" height="7"/><path d="M1 2.5l5 4 5-4"/></svg>dorian@marrowconstruction.com</p>
      <p class="line"><svg viewBox="0 0 12 12"><circle cx="6" cy="6" r="5"/><path d="M1 6h10M6 1c-2.5 3-2.5 7 0 10M6 1c2.5 3 2.5 7 0 10"/></svg>www.marrowconstruction.com</p>
    </div>
  </section>

  <section class="card card-back">
    <div class="back-mark" role="img" aria-label="Large faint company mark decoration"></div>
    <div class="services">
      <p><span class="lead">provided - </span>Roads, Substation Pads</p>
      <p>Temporary Pads, Site Pads</p>
      <p>Land Leveling</p>
      <div class="gap"></div>
      <p>Powerline Row Cleaning</p>
      <p>Land Clearing, Gates, Fencing</p>
      <p>Construction Entrances, Excavation</p>
      <p>Trenching, Underground Utilities</p>
      <p>Directional Boring, Pile Driving</p>
    </div>
    <div class="back-brand">
      <span class="brand-dot"></span>
      <span class="brand-name">Marrow Construction</span>
    </div>
  </section>
</body>
</html>
```